Bref créative
Business cards and stationery for innovative cloud apps comapany VORAX
VORAX sa
Use same font as used in my logo
Petros Lamvakis
VP & General Manager
Ermou Ave 27, Kifisia, 14671, Athens, Greece
petros@vorax-mail.gr
www.vorax-mail.gr
In the back we will have the same info in Greek
Name: Πέτρος Λαμβάκης
title: Γενικός Διευθυντής
address: Λεωφ. Ερμού 27, 14671, Κηφισιά, Αθήνα, Ελλάδα
phone: 0030 210 555 0147
cell: 0030 690 555 0293
fax: 0030 210 555 0148
email: petros@vorax-mail.gr
web address: www.vorax-mail.gr

```html
<!DOCTYPE html>
<html lang="en">
<head>
<meta charset="utf-8">
<title>VORAX business cards</title>
<link rel="stylesheet" href="https://fonts.googleapis.com/css2?family=Open+Sans:wght@400;600;700;800&display=swap">
<style>
  :root {
    --page-bg: #e9ebee;
    --card-bg: #ffffff;
    --card-shade: #f1f3f6;
    --brand-blue: #1f4fa6;
    --band-light: #3a9ee0;
    --band-dark: #1b6db5;
    --band-edge: #1c2f7c;
    --ink: #222630;
    --ink-soft: #4a4f5a;
    --divider: #c9ccd2;
  }
  * { box-sizing: border-box; margin: 0; padding: 0; }
  html, body { width: 1200px; height: 838px; overflow: hidden; }
  body {
    background: var(--page-bg);
    font-family: "Open Sans", Arial, sans-serif;
    color: var(--ink);
    position: relative;
  }
  .card {
    position: absolute;
    left: 280px;
    width: 640px;
    height: 360px;
    background: linear-gradient(160deg, var(--card-bg) 55%, var(--card-shade));
    box-shadow: 0 6px 18px rgba(20, 30, 60, 0.18);
    overflow: hidden;
  }
  .card--front { top: 48px; }
  .card--back { top: 438px; }

  .brand {
    position: absolute;
    left: 48px;
    top: 128px;
    display: flex;
    align-items: center;
    gap: 16px;
  }
  .brand__dot {
    width: 46px; height: 46px;
    border-radius: 50%;
    background: var(--brand-blue);
  }
  .brand__name {
    font-weight: 800;
    font-size: 62px;
    letter-spacing: 2px;
    color: var(--brand-blue);
    line-height: 1;
  }

  .divider {
    position: absolute;
    left: 352px;
    top: 72px;
    width: 1px;
    height: 196px;
    background: var(--divider);
  }

  .contact {
    position: absolute;
    left: 368px;
    top: 74px;
    width: 250px;
  }
  .contact__name {
    font-weight: 700;
    font-size: 21px;
    line-height: 1.15;
    color: var(--ink);
  }
  .contact__title {
    font-size: 12px;
    color: var(--ink-soft);
    margin-top: 2px;
  }
  .contact__address {
    font-size: 13.5px;
    line-height: 1.35;
    margin-top: 22px;
    color: var(--ink);
  }
  .contact__lines {
    list-style: none;
    margin-top: 12px;
    font-size: 13.5px;
    line-height: 1.45;
  }
  .contact__lines li { display: flex; align-items: center; gap: 6px; }
  .contact__icon { width: 13px; height: 13px; flex: none; fill: var(--ink); }

  .band {
    position: absolute;
    left: 0; right: 0; bottom: 0;
    height: 52px;
    background: linear-gradient(180deg, var(--band-light), var(--band-dark));
    border-top: 4px solid var(--band-edge);
    display: flex;
    align-items: center;
    padding-left: 44px;
  }
  .band__web {
    color: #ffffff;
    font-size: 14px;
    font-weight: 600;
    letter-spacing: 6px;
  }
</style>
</head>
<body>

<svg width="0" height="0" style="position:absolute" aria-hidden="true">
  <defs>
    <symbol id="icon-phone" viewBox="0 0 16 16">
      <path d="M3.5 1.5l2.5 0 1 3.5-1.6 1.2a8 8 0 0 0 4.4 4.4L11 9l3.5 1v2.5c0 1-1 2-2 2C6.5 14.5 1.5 9.5 1.5 3.5c0-1 1-2 2-2z"/>
    </symbol>
    <symbol id="icon-mobile" viewBox="0 0 16 16">
      <path d="M4.5 0.5h7a1 1 0 0 1 1 1v13a1 1 0 0 1-1 1h-7a1 1 0 0 1-1-1v-13a1 1 0 0 1 1-1zM5 2.5v9.5h6V2.5zM8 12.8a0.9 0.9 0 1 0 0 1.8a0.9 0.9 0 0 0 0-1.8z"/>
    </symbol>
    <symbol id="icon-fax" viewBox="0 0 16 16">
      <path d="M4 1h6l2 2v3H4zM1.5 6.5h13a1 1 0 0 1 1 1V13h-3v2h-9v-2h-3V7.5a1 1 0 0 1 1-1zM5 11v2.5h6V11z"/>
    </symbol>
    <symbol id="icon-mail" viewBox="0 0 16 16">
      <path d="M1 3h14v10H1zM2.5 4.5v0.4L8 8.8l5.5-3.9v-0.4zM2.5 6.7v4.8h11V6.7L8 10.6z"/>
    </symbol>
  </defs>
</svg>

<section class="card card--front" lang="en">
  <div class="brand">
    <span class="brand__dot"></span>
    <span class="brand__name">VORAX</span>
  </div>
  <div class="divider"></div>
  <div class="contact">
    <p class="contact__name">Petros Lamvakis</p>
    <p class="contact__title">VP &amp; General Manager</p>
    <p class="contact__address">Ermou Ave 27, Kifisia,<br>14671, Athens, Greece</p>
    <ul class="contact__lines">
      <li><svg class="contact__icon"><use href="#icon-phone"/></svg>: 0030 210 555 0147</li>
      <li><svg class="contact__icon"><use href="#icon-mobile"/></svg>: 0030 690 555 0293</li>
      <li><svg class="contact__icon"><use href="#icon-fax"/></svg>: 0030 210 555 0148</li>
      <li><svg class="contact__icon"><use href="#icon-mail"/></svg>: petros@vorax-mail.gr</li>
    </ul>
  </div>
  <div class="band"><span class="band__web">www.vorax-mail.gr</span></div>
</section>

<section class="card card--back" lang="el">
  <div class="brand">
    <span class="brand__dot"></span>
    <span class="brand__name">VORAX</span>
  </div>
  <div class="divider"></div>
  <div class="contact">
    <p class="contact__name">Πέτρος Λαμβάκης</p>
    <p class="contact__title">Γενικός Διευθυντής</p>
    <p class="contact__address">Λεωφ. Ερμού 27, 14671, Κηφισιά<br>Αθήνα, Ελλάδα</p>
    <ul class="contact__lines">
      <li><svg class="contact__icon"><use href="#icon-phone"/></svg>: 0030 210 555 0147</li>
      <li><svg class="contact__icon"><use href="#icon-mobile"/></svg>: 0030 690 555 0293</li>
      <li><svg class="contact__icon"><use href="#icon-fax"/></svg>: 0030 210 555 0148</li>
      <li><svg class="contact__icon"><use href="#icon-mail"/></svg>: petros@vorax-mail.gr</li>
    </ul>
  </div>
  <div class="band"><span class="band__web">www.vorax-mail.gr</span></div>
</section>

</body>
</html>
```